Business card for plumber

I need a business card for my plumbing company.
on it should:
Surname
position
E-mail
Telephone & mobile phone
Website
Please everything as placeholders / fantasy names.
We stand for high quality, hygiene and professionalism.

Colours:
# 606060 anthracite
# f7931e orange
# 2b89cc blue

Industry/Entity Type

Plumber

Contact Information for Business Card

folgt...

```html
<!DOCTYPE html>
<html lang="en">
<head>
<meta charset="utf-8">
<title>Kesselberg Haustechnik – Business Card</title>
<link href="https://fonts.googleapis.com/css2?family=Poppins:wght@400;500;700&display=swap" rel="stylesheet">
<style>
  :root {
    --anthracite: #606060;
    --orange: #f7931e;
    --blue: #2b89cc;
    --ink: #2e2e2e;
    --paper: #ffffff;
    --backdrop: #e9e7e3;
  }
  * { margin: 0; padding: 0; box-sizing: border-box; }
  html, body { width: 1200px; height: 900px; overflow: hidden; }
  body {
    background: var(--backdrop);
    font-family: "Poppins", sans-serif;
    position: relative;
  }
  .card {
    position: absolute;
    width: 540px;
    height: 340px;
    background: var(--paper);
    border-radius: 4px;
    box-shadow: 0 10px 28px rgba(0,0,0,.18);
    top: 280px;
  }
  .card--back { left: 40px; padding: 40px 44px; }
  .card--front {
    left: 620px;
    display: flex;
    flex-direction: column;
    align-items: center;
    justify-content: center;
    gap: 22px;
  }
  .brand {
    display: flex;
    align-items: center;
    gap: 10px;
    color: var(--blue);
    font-weight: 700;
    text-transform: uppercase;
    letter-spacing: .5px;
  }
  .brand__dot {
    width: 14px; height: 14px;
    border-radius: 50%;
    background: var(--orange);
  }
  .card--front .brand { font-size: 27px; }
  .card--back .brand { font-size: 17px; margin-bottom: 22px; }
  .tagline {
    font-size: 12.5px;
    font-weight: 500;
    color: var(--anthracite);
    letter-spacing: 1.2px;
    text-transform: uppercase;
  }
  .contact__name {
    color: var(--blue);
    font-weight: 700;
    font-size: 19px;
    margin-bottom: 14px;
  }
  .contact__list { list-style: none; }
  .contact__item {
    display: flex;
    align-items: flex-start;
    gap: 12px;
    font-size: 14px;
    line-height: 1.45;
    color: var(--ink);
    margin-bottom: 5px;
  }
  .contact__icon { width: 14px; height: 14px; margin-top: 3px; flex: none; fill: var(--blue); }
  .web__blue { color: var(--blue); }
  .web__orange { color: var(--orange); }
</style>
</head>
<body>

<section class="card card--back" aria-label="Business card, contact side">
  <div class="brand"><span class="brand__dot"></span>Kesselberg Haustechnik</div>
  <p class="contact__name">John Smith</p>
  <ul class="contact__list">
    <li class="contact__item">
      <svg class="contact__icon" viewBox="0 0 24 24"><path d="M12 2a7 7 0 0 0-7 7c0 5 7 13 7 13s7-8 7-13a7 7 0 0 0-7-7zm0 9.5A2.5 2.5 0 1 1 12 6.5a2.5 2.5 0 0 1 0 5z"/></svg>
      <span>Address, 303 location<br>City 79999</span>
    </li>
    <li class="contact__item">
      <svg class="contact__icon" viewBox="0 0 24 24"><path d="M6.6 10.8a15 15 0 0 0 6.6 6.6l2.2-2.2a1 1 0 0 1 1-.25 11.4 11.4 0 0 0 3.6.57 1 1 0 0 1 1 1V20a1 1 0 0 1-1 1A17 17 0 0 1 3 4a1 1 0 0 1 1-1h3.5a1 1 0 0 1 1 1c0 1.25.2 2.45.57 3.57a1 1 0 0 1-.25 1z"/></svg>
      <span>+99 999 9999</span>
    </li>
    <li class="contact__item">
      <svg class="contact__icon" viewBox="0 0 24 24"><path d="M7 1h10a2 2 0 0 1 2 2v18a2 2 0 0 1-2 2H7a2 2 0 0 1-2-2V3a2 2 0 0 1 2-2zm0 3v14h10V4z"/></svg>
      <span>+11 111 1111</span>
    </li>
    <li class="contact__item">
      <svg class="contact__icon" viewBox="0 0 24 24"><path d="M2 5h20v14H2zm2 2v.5l8 5 8-5V7l-8 5z"/></svg>
      <span>email@<span class="web__blue">kesselberg</span><span class="web__orange">haustechnik</span>.com</span>
    </li>
    <li class="contact__item">
      <svg class="contact__icon" viewBox="0 0 24 24"><circle cx="12" cy="12" r="10"/></svg>
      <span>www.<span class="web__blue">kesselberg</span><span class="web__orange">haustechnik</span>.com</span>
    </li>
  </ul>
</section>

<section class="card card--front" aria-label="Business card, brand side">
  <div class="brand"><span class="brand__dot"></span>Kesselberg Haustechnik</div>
  <p class="tagline">Plumbing | Heating24h Emergency Service | Maintenance</p>
</section>

</body>
</html>
```